Gift Cards in the Mail Envelope

Mailing out gift cards in the envelope. Need an eye popping envelope. Please look at the enclosed images. The envelope should look like that.

Low design quality

```html
<!DOCTYPE html>
<html lang="en">
<head>
<meta charset="utf-8">
<title>Gift Card Envelope</title>
<link rel="stylesheet" href="https://fonts.googleapis.com/css2?family=Quicksand:wght@700&family=Montserrat:ital,wght@0,500;0,700;1,500&display=swap">
<style>
  :root {
    --backdrop: #7d7f79;
    --paper: #f4f4f4;
    --paper-shade: #e6e6e6;
    --crease: #d2d2d2;
    --yellow: #ecd73a;
    --ink: #3d3d3d;
  }
  * { margin: 0; padding: 0; box-sizing: border-box; }
  html, body {
    width: 1200px;
    height: 982px;
    overflow: hidden;
    background: var(--backdrop);
  }
  .envelope {
    position: absolute;
    top: 363px;
    width: 332px;
    height: 229px;
    background: var(--paper);
    overflow: hidden;
  }
  .envelope--front { left: 252px; }
  .envelope--back { left: 627px; }

  .ribbon-art {
    position: absolute;
    inset: 0;
    width: 332px;
    height: 229px;
  }
  .headline {
    position: absolute;
    left: 16px;
    top: 58px;
    font-family: "Quicksand", sans-serif;
    font-weight: 700;
    font-size: 64px;
    line-height: 50px;
    letter-spacing: -1px;
  }
  .headline__gift { display: block; color: var(--yellow); }
  .headline__card { display: block; color: var(--ink); }

  .voucher {
    position: absolute;
    left: 17px;
    top: 197px;
    font-family: "Montserrat", sans-serif;
  }
  .voucher__label {
    color: var(--yellow);
    font-weight: 700;
    font-size: 6.4px;
    line-height: 8px;
  }
  .voucher__message {
    color: var(--ink);
    font-weight: 500;
    font-size: 6.6px;
    line-height: 9px;
  }

  .flap-lines {
    position: absolute;
    inset: 0;
    width: 332px;
    height: 229px;
  }
  .open-me {
    position: absolute;
    left: 0;
    right: 0;
    top: 54px;
    text-align: center;
    font-family: "Quicksand", sans-serif;
    font-weight: 700;
    font-size: 14px;
  }
  .open-me__open { color: var(--yellow); }
  .open-me__me { color: var(--ink); }
  .website-note {
    position: absolute;
    left: 0;
    right: 0;
    top: 206px;
    text-align: center;
    font-family: "Montserrat", sans-serif;
    font-style: italic;
    font-weight: 500;
    font-size: 5px;
    color: var(--ink);
  }
</style>
</head>
<body>

<section class="envelope envelope--front">
  <svg class="ribbon-art" viewBox="0 0 332 229" role="img" aria-label="Hand-drawn yellow ribbon tied in a bow across the envelope">
    <defs>
      <linearGradient id="ribbonTone" x1="0" y1="0" x2="1" y2="0">
        <stop offset="0" stop-color="#ecd73a" stop-opacity="0.25"/>
        <stop offset="0.6" stop-color="#ecd73a" stop-opacity="0.75"/>
        <stop offset="1" stop-color="#ecd73a" stop-opacity="0.9"/>
      </linearGradient>
    </defs>
    <polygon points="95,0 332,0 332,229 180,229 235,120" fill="url(#ribbonTone)"/>
  </svg>

  <h1 class="headline">
    <span class="headline__gift">Gift</span>
    <span class="headline__card">Card</span>
  </h1>

  <div class="voucher">
    <p class="voucher__label">VIRTUAL GIFT VOUCHER</p>
    <p class="voucher__message">You have received a Gift Card from us.</p>
  </div>
</section>

<section class="envelope envelope--back">
  <svg class="flap-lines" viewBox="0 0 332 229" aria-hidden="true">
    <path d="M0,0 L32,82 Q36,90 46,90 L286,90 Q296,90 300,82 L332,0 Z" fill="var(--paper)" stroke="var(--crease)" stroke-width="0.8"/>
    <line x1="34" y1="88" x2="2" y2="229" stroke="var(--crease)" stroke-width="0.8"/>
    <line x1="298" y1="88" x2="330" y2="229" stroke="var(--crease)" stroke-width="0.8"/>
  </svg>
  <p class="open-me"><span class="open-me__open">Open</span> <span class="open-me__me">Me</span></p>
  <p class="website-note">* More information on our website: (website address)</p>
</section>

</body>
</html>
```